Cafe - A FRAME Design

Need to create an A frame for my café.
Logo available
Word document - has basic information we think would be good.

Name: Brovvle Café

Notes from the A-frame printers.
File Requirements
• PDF without trim, crop or registration marks
• All files to be CMYK, not RGB
• All fonts converted to outlines (paths/curves)
• Embed all images and elements
• Files to be 100% scale unless otherwise specified
• 10mm Bleed
Resolution
• Bitmap images no less than 130 DPI at full size
Pantone Colours
• If required Pantone colours must be supplied

Target Market(s)

Mainly Students - University cafe

Requirements
Must have
• Cafe name: Brovvle
Nice to have
• Might be nice to have background - that orange color same as logo - just an idea

Word document - has basic idea regarding text that should be included

```html
<!DOCTYPE html>
<html lang="en">
<head>
<meta charset="utf-8">
<title>Brovvle Café – A-Frame</title>
<link rel="stylesheet" href="https://fonts.googleapis.com/css2?family=Montserrat:wght@800&family=Quicksand:wght@500;700&display=swap">
<style>
  :root {
    --stage: #2a2b2d;
    --slate: #454a53;
    --white: #ffffff;
    --orange: #f15a22;
    --wood-light: #b27a4e;
    --wood-mid: #9a6238;
    --wood-dark: #7a4a2a;
    --photo-warm: #8a5e3e;
    --photo-deep: #5a3a28;
    --photo-cream: #cdb59a;
    --photo-rose: #a8545e;
    --shadow: rgba(30, 20, 15, 0.75);
  }
  * { box-sizing: border-box; margin: 0; padding: 0; }
  html, body { width: 1200px; height: 675px; overflow: hidden; }
  body {
    background: var(--stage);
    display: flex; align-items: center; justify-content: center;
    font-family: "Quicksand", sans-serif;
  }
  .aframe {
    position: relative; width: 450px; height: 600px; overflow: hidden;
    box-shadow: 0 10px 30px rgba(0,0,0,0.5);
  }
  .wood {
    position: absolute; inset: 0;
    background: linear-gradient(90deg, var(--wood-mid), var(--wood-light) 35%, var(--wood-mid) 65%, var(--wood-dark));
  }
  .masthead {
    position: absolute; left: 0; top: 0; width: 100%; height: 105px;
    background: var(--slate); border-bottom: 4px solid var(--white);
    display: flex; align-items: center; justify-content: center; gap: 14px;
  }
  .brand-dot { width: 34px; height: 34px; border-radius: 50%; border: 3px solid var(--white); }
  .brand-name { color: var(--white); font-weight: 700; font-size: 44px; letter-spacing: -0.5px; }
  .headline {
    position: absolute; left: 0; top: 120px; width: 100%; text-align: center;
    font-family: "Montserrat", sans-serif; font-weight: 800; font-size: 25.5px;
    line-height: 32px; letter-spacing: -1px; color: var(--white);
    text-shadow: 2px 2px 3px var(--shadow);
  }
  .pill {
    position: absolute; height: 36px; border-radius: 18px;
    background: var(--slate); color: var(--white);
    border-right: 2px solid var(--orange); border-bottom: 2px solid var(--orange);
    font-size: 17.5px; font-weight: 500; line-height: 34px; white-space: nowrap;
    z-index: 1;
  }
  .photo {
    position: absolute; border-radius: 50%; border: 4px solid var(--orange);
    z-index: 2;
  }
  .photo--coffee { left: 328px; top: 193px; width: 112px; height: 112px; background: linear-gradient(160deg, var(--photo-warm), var(--photo-cream)); }
  .photo--food { left: 9px; top: 218px; width: 110px; height: 110px; background: linear-gradient(160deg, var(--photo-deep), var(--photo-warm)); }
  .photo--cake { left: 327px; top: 320px; width: 112px; height: 112px; background: linear-gradient(160deg, var(--photo-cream), var(--photo-deep)); }
  .photo--pastry { left: 11px; top: 392px; width: 106px; height: 106px; background: linear-gradient(160deg, var(--photo-cream), var(--photo-warm)); }
  .photo--catering { left: 330px; top: 449px; width: 108px; height: 108px; background: linear-gradient(160deg, var(--photo-deep), var(--photo-rose)); }
  .pill--coffee { left: 161px; top: 217px; width: 180px; padding-left: 17px; }
  .pill--food { left: 94px; top: 284px; width: 160px; padding-left: 36px; }
  .pill--vegan { left: 33px; top: 350px; width: 305px; padding-left: 12px; }
  .pill--pastry { left: 100px; top: 417px; width: 194px; padding-left: 22px; }
  .pill--catering { left: 153px; top: 483px; width: 190px; padding-left: 16px; }
  .location {
    position: absolute; left: 0; top: 558px; width: 318px; height: 40px;
    background: var(--orange); border-radius: 0 20px 20px 0;
    border-right: 2px solid var(--slate); border-bottom: 2px solid var(--slate);
    color: var(--white); font-weight: 700; font-size: 24px; line-height: 38px;
    padding-left: 25px; text-shadow: 1px 1px 2px var(--shadow);
  }
</style>
</head>
<body>
  <main class="aframe">
    <div class="wood" role="img" aria-label="Warm brown weathered timber plank background"></div>
    <header class="masthead">
      <span class="brand-dot"></span>
      <span class="brand-name">Brovvle</span>
    </header>
    <h1 class="headline">YOUR ENVIRONMENTALLY &amp;<br>SUSTAINABILITY FOCUSED CAFE</h1>

    <div class="pill pill--coffee">Specialty Coffee</div>
    <div class="photo photo--coffee" role="img" aria-label="Photo of a latte on a serving board"></div>

    <div class="pill pill--food">Fresh Food</div>
    <div class="photo photo--food" role="img" aria-label="Photo of fresh bread and coffee"></div>

    <div class="pill pill--vegan">(Vegan &amp; GF) Options Available</div>
    <div class="photo photo--cake" role="img" aria-label="Photo of a slice of chocolate cake"></div>

    <div class="pill pill--pastry">Pastries &amp; Drinks</div>
    <div class="photo photo--pastry" role="img" aria-label="Photo of a latte with doughnuts"></div>

    <div class="pill pill--catering">Catering Available</div>
    <div class="photo photo--catering" role="img" aria-label="Photo of a catering table spread"></div>

    <div class="location">Located @ Building 417</div>
  </main>
</body>
</html>
```